Attorney business card for two offices

Looking for a new business card design that can list both of my offices, one in Houston and one in West Texas. Want something masculine, easy to read, and conservative yet somewhat modern. Our current card has used a nautical star on it for years, but I am not necessarily attached to that. Also, a lot of our forms use dark green and orange. Second office address is P.O. Box 518, Marathon, Texas 79617

```html
<!DOCTYPE html>
<html lang="en">
<head>
<meta charset="utf-8">
<title>Daniel R. Whitmore, Sr — Business Card</title>
<link rel="stylesheet" href="https://fonts.googleapis.com/css2?family=Libre+Baskerville:wght@700&family=Libre+Franklin:wght@500;600&display=swap">
<style>
  :root {
    --page-bg: #e4e4e4;
    --card-bg: #4a4c47;
    --gold: #e8b33e;
    --ink: #111111;
    --paper-white: #ffffff;
  }
  * { box-sizing: border-box; margin: 0; padding: 0; }
  html, body {
    width: 1200px;
    height: 900px;
    overflow: hidden;
    background: var(--page-bg);
  }
  .card {
    position: absolute;
    left: 60px;
    top: 150px;
    width: 1080px;
    height: 600px;
    background: var(--card-bg);
    color: var(--paper-white);
    font-family: "Libre Franklin", Arial, sans-serif;
  }
  .brand-mark {
    position: absolute;
    left: 40px;
    top: 150px;
    display: flex;
    align-items: center;
    gap: 14px;
  }
  .brand-mark__dot {
    width: 34px;
    height: 34px;
    border-radius: 50%;
    background: var(--gold);
  }
  .brand-mark__name {
    font-weight: 600;
    font-size: 30px;
    letter-spacing: 0.06em;
    color: var(--gold);
  }
  .attorney-name {
    position: absolute;
    left: 224px;
    top: 78px;
    width: 830px;
    text-align: right;
    font-family: "Libre Baskerville", Georgia, serif;
    font-weight: 700;
    font-size: 50px;
    line-height: 1;
    color: var(--ink);
    -webkit-text-stroke: 1.5px var(--paper-white);
    paint-order: stroke fill;
  }
  .attorney-title {
    position: absolute;
    left: 366px;
    top: 164px;
    font-family: "Libre Baskerville", Georgia, serif;
    font-weight: 700;
    font-size: 33px;
    line-height: 1;
    color: var(--ink);
    -webkit-text-stroke: 1.2px var(--paper-white);
    paint-order: stroke fill;
  }
  .firm {
    position: absolute;
    left: 369px;
    top: 248px;
  }
  .firm__name {
    font-weight: 600;
    font-size: 33px;
    line-height: 1.05;
  }
  .firm__tagline {
    font-weight: 500;
    font-size: 22px;
    font-variant: small-caps;
    line-height: 1.1;
  }
  .contact {
    position: absolute;
    left: 28px;
    top: 465px;
  }
  .contact__email {
    font-weight: 500;
    font-size: 19px;
    text-transform: uppercase;
    margin-bottom: 18px;
  }
  .contact__phone {
    font-weight: 500;
    font-size: 26px;
    line-height: 1.4;
  }
  .offices {
    position: absolute;
    right: 34px;
    top: 512px;
    text-align: right;
    font-weight: 500;
    font-size: 26px;
    line-height: 1.4;
    font-variant: small-caps;
  }
  .offices__label { font-size: 21px; }
</style>
</head>
<body>
  <article class="card">
    <div class="brand-mark">
      <span class="brand-mark__dot"></span>
      <span class="brand-mark__name">WHITMORE</span>
    </div>

    <h1 class="attorney-name">DANIEL R. WHITMORE, SR</h1>
    <p class="attorney-title">ATTORNEY AT LAW</p>

    <div class="firm">
      <p class="firm__name">THE WHITMORE LAW FIRM, P.C.</p>
      <p class="firm__tagline">Power of Attorney and Fee Agreement</p>
    </div>

    <div class="contact">
      <p class="contact__email">daniel@bayoulawtx.com</p>
      <p class="contact__phone">T. 713.555.0142</p>
      <p class="contact__phone">F. 832.555.0187</p>
    </div>

    <div class="offices">
      <p>4810 Westpark Drive, Houston, Texas 77027</p>
      <p><span class="offices__label">second office :</span> P.O. Box 518, Marathon, Texas 79617</p>
    </div>
  </article>
</body>
</html>
```